Redesign PixelHarbor's Designer Account Home Page

Are a web designer? New to PixelHarbor? This contest is for you!

We want you to redesign PixelHarbor's designer account home page. We're looking for bold and innovative ideas to make this page a useful and fun experience for you and your fellow designers.

Only new registrants this month are eligible to enter this contest and win prizes.

Your task:
* We want you to put your web design skills to the test and re-design the My Account home page ("Overview") on PixelHarbor to make it more functional and engaging for designers on PixelHarbor.
* The page you are redesigning is here: http://www.pixelharbor-example.com/my-profile.
* Your design should allow for the same functionality as the existing page, though you don't need to replicate the same elements (buttons) or the same menu structure.
* Your design must fit with the branding of the site.
* You must provide a brief outline of what changes you made and why when you upload your design
* 1 submission per designer - make it your best work!
* Pls see "Must haves" for requirements.

Deadline:
* Submit before 12:00am 1st September UTC. Pls convert this deadline to your local timezone and take note of the local time and date

Prizes: $1,000 to win
* First prize for the best design is $700
* Second prize is $200
* Third prize is $100

If you started from scratch, how would you design the MyAccount page on PixelHarbor?

Good luck & have fun!

Mel / The PixelHarbor Team

Target Market(s)

PixelHarbor designers

Number of Pages Required

1 page

Requirements
Must have
• Dimensions: 1200 x 1000 px
• Minimum 150-300 dpi
• Your design must adhere to our quality standards to be eligible to receive a prize
• Submissions must be created in Adobe Creative Suite (Illustrator or Photoshop)
• Your design must fit with the branding of the PixelHarbor site.
• Only new registrants this month are eligible to enter and win prizes.

```html
<!DOCTYPE html>
<html lang="en">
<head>
<meta charset="utf-8">
<title>PixelHarbor – My Account Overview</title>
<link href="https://fonts.googleapis.com/css2?family=Open+Sans:wght@400;600;700&display=swap" rel="stylesheet">
<style>
:root{
  --ink:#333;
  --muted:#888;
  --line:#dcdcdc;
  --page:#ffffff;
  --band:#ececec;
  --dark:#2c2c2c;
  --darker:#1f1f1f;
  --blue:#2a9fd6;
  --green:#7cb927;
  --bar:#d9d9d9;
}
*{box-sizing:border-box;margin:0;padding:0}
html,body{width:839px;height:1200px;overflow:hidden}
body{font-family:"Open Sans",Arial,sans-serif;color:var(--ink);background:var(--page);font-size:8px;position:relative}
.wrap{width:799px;margin:0 auto}

/* header */
.topbar{background:var(--dark);height:24px;color:#ddd}
.topbar .wrap{display:flex;align-items:center;height:24px;gap:12px}
.brand{display:flex;align-items:center;gap:4px;font-weight:700;font-size:12px;color:#fff}
.brand-dot{width:10px;height:10px;border-radius:50%;background:var(--blue)}
.mainnav{display:flex;gap:9px;font-size:7px}
.phone{margin-left:auto;font-size:7px}
.flag{width:12px;height:8px;background:#4a6aa5}
.search{width:60px;height:14px;background:#fff;border-radius:2px;color:#555;font-size:7px;padding:2px 4px}
.btn-green{background:var(--green);color:#fff;font-size:7px;padding:3px 7px;border-radius:2px}

.crumbs{height:18px;display:flex;align-items:center;gap:10px;font-size:7px;color:#666;border-bottom:1px solid var(--line)}

.tabs{display:flex;height:22px;margin-top:4px;background:#f3f3f3;border:1px solid var(--line)}
.tab{display:flex;align-items:center;gap:3px;padding:0 9px;font-size:7.5px;color:#555;border-right:1px solid var(--line)}
.tab i{width:7px;height:7px;background:#bbb;border-radius:1px;display:inline-block}
.tab.active{background:var(--blue);color:#fff}
.tab.active i{background:#fff}

h1{font-size:14px;font-weight:600;margin:14px 0 8px}
.stats{background:var(--dark);height:34px;display:flex;align-items:center;gap:12px;padding:0 10px;color:#ccc;font-size:8px}
.avatar{width:22px;height:22px;border-radius:50%;background:#555;border:2px solid #777}
.stats b{color:var(--blue);font-size:10px}
.stats .pct{color:#fff}

.band{background:var(--band);height:10px;margin-top:14px}

.section-head{display:flex;justify-content:space-between;align-items:baseline;margin-top:12px}
h2{font-size:10px;color:var(--blue);font-weight:600}
.progress{height:20px;background:var(--bar);margin-top:6px;border-radius:2px;position:relative;overflow:hidden}
.progress span{position:absolute;left:0;top:0;bottom:0;width:57%;background:#c6c6c6}
h3{font-size:10px;font-weight:600;margin:10px 0 4px}
.todo{list-style:none}
.todo li{display:flex;align-items:center;height:15px;border-bottom:1px solid #eee;font-size:7.5px;padding-left:4px;gap:5px}
.todo li::before{content:"";width:6px;height:6px;border-radius:50%;background:#999}
.todo .end{margin-left:auto}
.pill{background:#e2e2e2;border:1px solid #ccc;font-size:6.5px;padding:1px 6px;border-radius:2px}

.cols-area{background:var(--band);margin-top:24px;padding:30px 0 30px}
.cols{display:flex;gap:20px}
.card{flex:1;background:#fff;border:1px solid var(--line)}
.card h2{padding:8px 10px;border-bottom:1px solid var(--line);font-size:10px}
.card .intro{font-size:7px;color:var(--muted);padding:8px 10px}
.job{display:flex;gap:8px;padding:8px 10px;border-top:1px solid #f0f0f0}
.job-dot{width:12px;height:12px;border-radius:50%;background:var(--blue);flex:none;margin-top:2px}
.job p{font-size:7.5px;line-height:1.35}
.job small{font-size:6.5px;color:var(--muted)}
.pager{display:flex;justify-content:space-between;font-size:7px;color:var(--blue);padding:8px 10px;border-top:1px solid var(--line)}
.ach{display:flex;gap:8px;align-items:center;padding:9px 10px;border-top:1px solid #f0f0f0}
.ach-badge{width:18px;height:18px;border-radius:50%;background:#777;flex:none}
.ach p{font-size:7.5px;font-weight:600}
.ach small{display:block;font-size:6.5px;color:var(--muted);font-weight:400}

/* footer */
.footer{background:var(--dark);color:#bbb;position:absolute;left:0;right:0;top:690px;bottom:0}
.footer .wrap{display:flex;gap:26px;padding-top:28px}
.fcol h4{color:#fff;font-size:10px;margin-bottom:10px}
.fcol ul{list-style:none}
.fcol li{font-size:7px;line-height:16px}
.tags{display:flex;flex-wrap:wrap;gap:4px;width:140px}
.tags span{background:#444;font-size:6.5px;padding:2px 5px;border-radius:2px}
.news{margin-left:auto;width:150px}
.news-row{display:flex;gap:3px}
.news-row .input{flex:1;height:14px;background:#fff;border-radius:2px}
.socials{display:flex;flex-wrap:wrap;gap:6px;margin-top:14px;width:110px}
.socials span{width:20px;height:20px;border-radius:50%}
.fbrand{margin-top:14px;display:flex;align-items:center;gap:5px;font-size:14px;font-weight:700;color:#fff}
.fbrand i{width:14px;height:14px;border-radius:50%;background:var(--blue)}
.copy{position:absolute;left:0;right:0;bottom:0;height:50px;background:var(--darker);font-size:6.5px;color:#888;text-align:center;padding-top:18px}
</style>
</head>
<body>
<header class="topbar">
  <div class="wrap">
    <div class="brand"><span class="brand-dot"></span>PixelHarbor</div>
    <nav class="mainnav"><span>Categories</span><span>Designers</span><span>Browse Jobs</span><span>How it works</span></nav>
    <span class="phone">1800 555 014</span>
    <span class="flag" role="img" aria-label="Country flag"></span>
    <span class="search">My Profile ▾</span>
    <span class="btn-green">Browse Jobs</span>
  </div>
</header>

<main class="wrap">
  <div class="crumbs"><span>Home</span><span>My Profile</span></div>
  <nav class="tabs">
    <span class="tab active"><i></i>Overview</span>
    <span class="tab"><i></i>Notifications (0)</span>
    <span class="tab"><i></i>Invites (0)</span>
    <span class="tab"><i></i>Submissions (0)</span>
    <span class="tab"><i></i>Messages (0)</span>
    <span class="tab"><i></i>Watchlist (0)</span>
    <span class="tab"><i></i>Widgets</span>
    <span class="tab"><i></i>My Profile</span>
  </nav>

  <h1>Overview</h1>
  <div class="stats">
    <span class="avatar" role="img" aria-label="Profile picture placeholder"></span>
    <span>Rank <b>#408171</b> (of 874,098 designers)</span>
    <span>Position <b class="pct">0%</b></span>
    <span>Submissions <b>0</b> (site average: 9)</span>
    <span>Earnings <b>$0.00</b> (site average: $128.48)</span>
  </div>
</main>

<div class="band"></div>

<section class="wrap">
  <div class="section-head"><h2>Getting Started - Complete Your Profile</h2><span>57% complete</span></div>
  <div class="progress"><span></span></div>
  <h3>Things left to do:</h3>
  <ul class="todo">
    <li>Tell us what type of designer you are<svg class="end" width="10" height="10" viewBox="0 0 10 10"><path d="M1 5l3 3 5-7" fill="none" stroke="#222" stroke-width="1.8"/></svg></li>
    <li>Verify your payment address<svg class="end" width="10" height="10" viewBox="0 0 10 10"><path d="M1 5l3 3 5-7" fill="none" stroke="#222" stroke-width="1.8"/></svg></li>
    <li>Visit the Jobs Board<svg class="end" width="10" height="10" viewBox="0 0 10 10"><path d="M1 5l3 3 5-7" fill="none" stroke="#222" stroke-width="1.8"/></svg></li>
    <li>Add your profile pic<span class="end pill">Complete</span></li>
    <li>Add an about me to your profile<svg class="end" width="10" height="10" viewBox="0 0 10 10"><path d="M1 5l3 3 5-7" fill="none" stroke="#222" stroke-width="1.8"/></svg></li>
    <li>Review and accept the PixelHarbor quality standards<span class="end pill">Complete</span></li>
    <li>Submit your first design<span class="end pill">Complete</span></li>
  </ul>
</section>

<section class="cols-area">
  <div class="wrap cols">
    <div class="card">
      <h2>Recommended Jobs</h2>
      <p class="intro">Jump in early: these open jobs have no entries yet and need your ideas.</p>
      <div class="job"><span class="job-dot"></span><p>New logo for a small bakery that sells fresh bread and cakes<br><small>5 Days Left | 0 | $410 | Watchlist</small></p></div>
      <div class="job"><span class="job-dot"></span><p>Landing page for a yoga studio launching new weekly classes<br><small>5 Days Left | 0 | $410 | Watchlist</small></p></div>
      <div class="job"><span class="job-dot"></span><p>Business card design for a family owned plumbing company<br><small>5 Days Left | 0 | $410 | Watchlist</small></p></div>
      <div class="job"><span class="job-dot"></span><p>Packaging label for an organic honey brand with a warm feel<br><small>5 Days Left | 0 | $410 | Watchlist</small></p></div>
      <div class="pager"><span>Page 1</span><span>Previous &nbsp; Next</span></div>
    </div>
    <div class="card">
      <h2>Achievements</h2>
      <p class="intro">Earn PixelHarbor achievements as you unlock new milestones.</p>
      <div class="ach"><span class="ach-badge"></span><p>Rookie (Basic)<small>Submit at least 1 design to contests</small></p></div>
      <div class="ach"><span class="ach-badge"></span><p>Rookie (Basic)<small>Submit at least 1 design to contests</small></p></div>
      <div class="ach"><span class="ach-badge"></span><p>Rookie (Basic)<small>Submit at least 1 design to contests</small></p></div>
      <div class="ach"><span class="ach-badge"></span><p>Rookie (Basic)<small>Submit at least 1 design to contests</small></p></div>
    </div>
  </div>
</section>

<footer class="footer">
  <div class="wrap">
    <div class="fcol"><h4>I need a...</h4><ul><li>Logo design</li><li>Website design</li><li>Business card</li><li>Brochure design</li><li>Flyer design</li><li>T-shirt design</li><li>Banner ads</li><li>Packaging</li></ul></div>
    <div class="fcol"><h4>Find a...</h4><ul><li>Logo designer</li><li>Web designer</li><li>Graphic designer</li><li>Illustrator</li><li>Print designer</li><li>Freelancer</li><li>Design studio</li><li>Design agency</li></ul></div>
    <div class="fcol"><h4>About us</h4><ul><li>Our story</li><li>Careers</li><li>Contact us</li><li>Press</li><li>Blog</li><li>Help centre</li><li>Terms of use</li><li>Privacy</li></ul></div>
    <div class="fcol"><h4>Popular pages</h4>
      <div class="tags"><span>Design contests</span><span>Logo ideas</span><span>Web templates</span><span>Brand names</span><span>Print shops</span><span>Top designers</span><span>Pricing</span><span>Showcase</span></div>
    </div>
    <div class="news">
      <div class="fcol"><h4>Subscribe to our newsletter</h4></div>
      <div class="news-row"><span class="input"></span><span class="btn-green">Join</span></div>
      <div class="socials">
        <span style="background:#3b8fd1" role="img" aria-label="Social link"></span>
        <span style="background:#3b5a99" role="img" aria-label="Social link"></span>
        <span style="background:#d23f31" role="img" aria-label="Social link"></span>
        <span style="background:#e07a1f" role="img" aria-label="Social link"></span>
        <span style="background:#1c7cb5" role="img" aria-label="Social link"></span>
        <span style="background:#c8232c" role="img" aria-label="Social link"></span>
        <span style="background:#6aa52f" role="img" aria-label="Social link"></span>
        <span style="background:#888" role="img" aria-label="Social link"></span>
      </div>
      <div class="fbrand"><i></i>PixelHarbor</div>
    </div>
  </div>
  <div class="copy">Copyright © PixelHarbor Pty Ltd. All rights reserved. Use of this site means you accept our terms and privacy policy.</div>
</footer>
</body>
</html>
```